THE PRACTICE NAME "The Renal Crest MD" FOR A NEW MEDICAL PRACTICE STARTUP

THIS IS A BUSINESS CARD REQUEST FOR A KIDNEY DOCTOR's(NEPHROLOGIST) PRACTICE, THIS PRACTICE WILL BE IN EL PASO,TEXAS USA.OPEN TO INNOVATIVE IDEAS!

THE RENAL CREST MD ( NAME OF PRACTICE)

VIKRANT L. MOTHRE, MD FNKF FASN ( NAME OF PHYSICIAN WITH DEGREES)
BOARD CERTIFIED INTERNAL MEDICINE
BOARD CERTIFIED NEPHROLOGY
HYPERTENSION SPECIALIST

OFFICE ADDRESS, PHONE, FAX AND EMAIL PENDING

Guarding Health. Building Futures.(MOTTO) THE LOGO SHOILD REFLECT THIS MESSAGE. WE NEED A LOGO DESIGN WITH 2 KIDNEYS OR CAN BE ONE KIDNEY ALSO.

Target Market(s)

PATIENTS WITH KIDNEY DISEASE, HYPERTENSION, ENGLISH AND SPANISH SPEAKING POPULATION AND PATIENTS ON DIALYSIS

Industry/Entity Type

Health Care

Contact Information for Business Card

HYPERTENSION SPECIALIST

WEBSITE URL PENDING

Font styles to use
Serif
Sans Serif
Script

Colors
fbed38
ffc214
fbf289
fbee3e
5c5c5c
333333
1b1b1b
757575
d3d3d3

Requirements
Must have
• A KIDNEY LOGO
• NAME OF THE PRACTICE
Nice to have
• IF THE CARD CAN BE IN THE SHAPE OF A KIDNEY

```html
<!DOCTYPE html>
<html lang="en">
<head>
<meta charset="utf-8">
<title>The Renal Crest MD — Business Cards</title>
<link rel="stylesheet" href="https://fonts.googleapis.com/css2?family=Raleway:ital,wght@0,300;0,400;1,300&family=Quicksand:wght@400&display=swap">
<style>
  :root {
    --backdrop: #e4e4e2;
    --paper: #ffffff;
    --sun: #fbdf2a;
    --sun-light: #fbee3e;
    --accent: #f5c800;
    --ink-dark: #1b1b1b;
    --ink: #5c5c5c;
    --ink-soft: #757575;
    --ink-faint: #b5b5b5;
    --white: #ffffff;
  }
  * { box-sizing: border-box; margin: 0; padding: 0; }
  html, body { width: 1200px; height: 1200px; overflow: hidden; }
  body {
    background: var(--backdrop);
    font-family: "Raleway", sans-serif;
    position: relative;
  }
  .card {
    position: absolute;
    top: 240px;
    width: 420px;
    height: 720px;
    border-radius: 210px;
    padding: 70px 50px 0 56px;
    display: flex;
    flex-direction: column;
    align-items: center;
  }
  .card--white { left: 140px; background: var(--paper); }
  .card--yellow { left: 640px; background: linear-gradient(160deg, var(--sun) 0%, var(--sun-light) 100%); }

  .brand-mark { display: flex; flex-direction: column; align-items: center; gap: 14px; }
  .brand-mark__dot { width: 64px; height: 64px; border-radius: 50%; background: var(--accent); }
  .card--yellow .brand-mark__dot { background: var(--white); }
  .brand-mark__name {
    font-weight: 300; font-size: 20px; letter-spacing: -0.5px; color: var(--ink);
  }
  .card--yellow .brand-mark__name { color: var(--ink); }

  .motto {
    margin-top: 38px;
    font-family: "Quicksand", sans-serif;
    font-size: 15px; letter-spacing: 2px; color: var(--ink-faint);
    white-space: nowrap;
  }
  .card--yellow .motto { color: var(--ink-soft); }

  .physician {
    align-self: stretch;
    margin-top: 42px;
    border-left: 3px solid var(--accent);
    padding: 4px 0 4px 12px;
  }
  .card--yellow .physician { border-left-color: var(--ink); }
  .physician__name { font-size: 17px; font-weight: 400; color: var(--ink-dark); letter-spacing: -0.4px; }
  .card--yellow .physician__name { color: var(--white); }
  .physician__title { font-size: 17px; font-style: italic; font-weight: 300; color: var(--ink-faint); line-height: 1.45; }
  .card--yellow .physician__title { color: #fff7b8; }

  .contact { align-self: stretch; margin-top: 32px; font-size: 17px; font-weight: 300; color: var(--ink-dark); line-height: 1.9; }
  .contact__label { color: var(--ink-soft); font-size: 15px; margin-right: 6px; }
  .contact__fax { margin-left: 18px; }
  .card--yellow .contact, .card--yellow .contact__label { color: var(--white); }

  .address { align-self: stretch; margin-top: 18px; font-size: 18px; font-weight: 300; color: var(--ink-dark); line-height: 1.4; }
  .card--yellow .address { color: var(--white); }

  .website { margin-top: 56px; font-size: 17px; font-style: italic; font-weight: 300; color: var(--accent); }
  .card--yellow .website { color: var(--white); }
</style>
</head>
<body>
  <article class="card card--white">
    <div class="brand-mark">
      <span class="brand-mark__dot"></span>
      <span class="brand-mark__name">THE RENAL CREST MD</span>
    </div>
    <p class="motto">Guarding Health. Building Futures.</p>
    <section class="physician">
      <p class="physician__name">VIKRANT L. MOTHRE, MD FNKF FASN</p>
      <p class="physician__title">Board Certified Internal Medicine</p>
      <p class="physician__title">Board Certified Nephrology</p>
      <p class="physician__title">Hypertension Specialist</p>
    </section>
    <section class="contact">
      <p><span class="contact__label">TEL:</span>012 345 678 <span class="contact__fax"><span class="contact__label">FAX:</span>012 345 678 12</span></p>
      <p><span class="contact__label">E-MAIL:</span>office@renalcrest.example</p>
    </section>
    <p class="address">Office Address Goes Here, Number<br>Building 0123</p>
    <p class="website">www.renalcrestmd.example</p>
  </article>

  <article class="card card--yellow">
    <div class="brand-mark">
      <span class="brand-mark__dot"></span>
      <span class="brand-mark__name">THE RENAL CREST MD</span>
    </div>
    <p class="motto">Guarding Health. Building Futures.</p>
    <section class="physician">
      <p class="physician__name">VIKRANT L. MOTHRE, MD FNKF FASN</p>
      <p class="physician__title">Board Certified Internal Medicine</p>
      <p class="physician__title">Board Certified Nephrology</p>
      <p class="physician__title">Hypertension Specialist</p>
    </section>
    <section class="contact">
      <p><span class="contact__label">TEL:</span>012 345 678 <span class="contact__fax"><span class="contact__label">FAX:</span>012 345 678 12</span></p>
      <p><span class="contact__label">E-MAIL:</span>office@renalcrest.example</p>
    </section>
    <p class="address">Office Address Goes Here, Number<br>Building 0123</p>
    <p class="website">www.renalcrestmd.example</p>
  </article>
</body>
</html>
```